Modes of Action Brochure/Handout

We need an innovative, professional design for a multi page presentation of our research findings. We want a clean, fresh layout, want to utilize a couple photos we have bought and included in the example we put together for a starting point.. We want it to read easily.

Target Market(s)

Dietary Supplement Industry

Industry/Entity Type

It Professional

Requirements
Must have
• Attention getting, attractive.

```html
<!DOCTYPE html>
<html lang="en">
<head>
<meta charset="utf-8">
<title>Vitalis V12 — Modes of Action Brochure</title>
<link rel="stylesheet" href="https://fonts.googleapis.com/css2?family=Oswald:wght@400;500&family=Open+Sans:wght@400;600;700&display=swap">
<style>
  :root {
    --red: #c8161d;
    --red-deep: #9e0f14;
    --gold: #f5c21b;
    --ink: #2b2b2b;
    --page: #ffffff;
    --page-shade: #ececec;
    --backdrop: #ffffff;
    --label: #c0281e;
    --strip: #f1e6c8;
    --accent-blue: #1e73d8;
  }
  * { box-sizing: border-box; margin: 0; padding: 0; }
  html, body { width: 1200px; height: 900px; overflow: hidden; background: var(--backdrop); }
  body { font-family: "Open Sans", Arial, sans-serif; color: var(--ink); position: relative; }

  .caption { position: absolute; font-family: "Oswald", "Arial Narrow", sans-serif; color: var(--label); text-align: center; }
  .caption--top { top: 8px; left: 0; width: 1200px; font-size: 15px; }
  .caption--bottom { top: 860px; width: 280px; font-size: 21px; }

  .spread { position: absolute; left: 180px; display: flex; box-shadow: 0 2px 10px rgba(0,0,0,.18); }
  .spread--inside { top: 34px; }
  .spread--outside { top: 458px; }

  .page {
    width: 280px; height: 396px; position: relative; overflow: hidden;
    background: linear-gradient(90deg, var(--page) 0%, var(--page) 88%, var(--page-shade) 100%);
    padding: 10px 12px; font-size: 5.6px; line-height: 1.45;
  }
  .page + .page { border-left: 1px solid #ddd; }

  .photo { display: block; }
  .photo--framed { border: 1.5px solid var(--red); }

  .heading {
    display: inline-block; background: var(--red); color: #fff;
    font-weight: 700; font-size: 7px; text-transform: uppercase;
    padding: 2px 18px 2px 4px; margin: 6px 0 3px;
    border-bottom: 1.5px solid var(--gold);
  }
  .heading--gold { color: var(--gold); text-transform: none; width: 100%; }
  .lede { font-weight: 700; font-size: 5.8px; margin-bottom: 2px; }
  .physiology b { color: var(--red); }
  p { margin-bottom: 2px; }

  .two-col { display: flex; gap: 8px; }
  .two-col > div { flex: 1; }
  .mode { display: flex; gap: 4px; }
  .mode .photo { flex: 0 0 36px; height: 36px; }
  .observation { font-size: 6.6px; line-height: 1.5; }

  .refs { list-style: none; }
  .refs li { position: relative; padding-left: 8px; margin-bottom: 3.5px; font-size: 5.4px; }
  .refs li::before { content: ""; position: absolute; left: 0; top: 1.5px; border-left: 4px solid var(--ink); border-top: 2.5px solid transparent; border-bottom: 2.5px solid transparent; }

  .back-cover { padding: 0; background: linear-gradient(160deg, #d81f24 0%, var(--red) 50%, var(--red-deep) 100%); }
  .back-cover .photo { position: absolute; inset: 0; }
  .back-footer {
    position: absolute; left: 8px; right: 8px; bottom: 10px; height: 26px;
    background: var(--strip); display: flex; align-items: center; padding: 0 32px 0 6px; font-size: 5.6px;
  }
  .back-footer .tab { position: absolute; right: 0; top: 0; bottom: 0; width: 26px; background: var(--accent-blue); }

  .front-cover { padding: 0; }
  .front-cover .photo { position: absolute; inset: 0; }
  .tagline-band {
    position: absolute; left: 0; right: 0; top: 232px; height: 26px;
    background: rgba(255,255,255,.9); display: flex; align-items: center; justify-content: space-between; padding: 0 8px 0 14px;
    white-space: nowrap;
  }
  .tagline { font-weight: 700; font-size: 6.8px; color: var(--red-deep); }
  .brand { display: flex; align-items: center; gap: 3px; font-weight: 700; font-size: 6.8px; color: var(--red); }
  .brand .mark { width: 6px; height: 6px; background: var(--red); }
</style>
</head>
<body>

<div class="caption caption--top">Trifold A4 size</div>

<section class="spread spread--inside">
  <article class="page page--intro">
    <div class="photo photo--framed" role="img" aria-label="Photo of a woman with open arms on a beach at sunset, sea rock behind her" style="height:150px;background:linear-gradient(180deg,#d9e3ea 0%,#b9c6cf 45%,#e8e0cf 70%,#8d8a80 100%);"></div>
    <div class="two-col">
      <div>
        <h2 class="heading heading--gold">Modes of Action</h2>
        <div class="mode">
          <div class="photo" role="img" aria-label="Microscope image of immune cells" style="background:linear-gradient(135deg,#3a3f55,#9a2d36);"></div>
          <p>Ground-breaking research, life science patents awarded, published double-blind placebo controlled human trials with healthy human adults, published animal studies, published in vitro studies.</p>
        </div>
        <p>consumer reports and anecdotal evidence from around the world confirm benefits and help the makers to refine the formula.</p>
      </div>
      <div>
        <h2 class="heading heading--gold">Important General Observation</h2>
        <p class="observation">Vitalis V12 functions very uniquely as a normalizing and modulating agent to numerous aspects of the immune response. This novel capability is not offered by any other dietary supplement ingredient and is the reason consumers find the supplement of such value in daily life.</p>
      </div>
    </div>
    <h2 class="heading">Innate Immunity</h2>
    <p class="physiology"><b>PHYSIOLOGY:</b> The innate immune system is the body's first line of defense. It responds in a generic way and is the earliest response to antigens. Vitalis V12 supports the effective, balanced activity of these first responders and recommended daily use.</p>
    <h2 class="heading heading--gold" style="width:auto">Executive Summary</h2>
    <div class="photo" role="img" aria-label="Small laboratory photo" style="width:40px;height:36px;background:linear-gradient(135deg,#5d8fb0,#c9dbe6);"></div>
  </article>

  <article class="page page--research">
    <h2 class="heading">Inflammatory Response</h2>
    <p class="lede">Provides direct support to cells critical to the immune response and significant support to C-reactive protein (CRP) gene expression.</p>
    <p class="physiology"><b>PHYSIOLOGY:</b> Inflammation reflects the most fundamental protective immune response. It involves tight regulation of immune cells, blood vessels, and molecular mediators. The purpose of inflammation is to eliminate the initial cause of cell injury, clear out necrotic cells and tissues damaged from the original insult and the inflammatory process, and to initiate tissue repair. The process of acute inflammation is initiated by resident immune cells already present in the involved tissue.</p>
    <h2 class="heading">Apoptosis</h2>
    <p class="lede">Supports regulated apoptosis.</p>
    <p class="physiology"><b>PHYSIOLOGY:</b> Professional phagocytes of the immune system are critical to the process of apoptosis. Apoptosis is the process of programmed cell death (PCD) that occurs in multicellular organisms. Biochemical events lead to characteristic cell changes (morphology) and death. These changes include blebbing, cell shrinkage, nuclear fragmentation, chromatin condensation, and chromosomal DNA fragmentation. Phagocytes are cells that protect the body by ingesting (phagocytosing) harmful foreign particles, bacteria, and dead or dying cells.</p>
    <h2 class="heading">Cellular Communication</h2>
    <p class="lede">Supports effective cellular communication.</p>
    <p class="physiology"><b>PHYSIOLOGY:</b> Cell signaling is part of a complex system of communication that governs basic cellular activities and coordinates cell actions. The ability of cells to perceive and correctly respond to their microenvironment is the basis of development, tissue repair, and immunity as well as normal tissue homeostasis. Vitalis V12's support for cellular signaling comes from two distinct sources. Sequencing of Vitalis V12 at Eastbrook University revealed the full array of cell signaling molecules that are present. These molecules are easily absorbed and ready to use. At the same time, product research demonstrates that Vitalis V12 can initiate the immune cascade and thereby lead to the production of new cellular signaling molecules. This was most highly apparent in a study performed at Westmont University and is also demonstrated in several Vitalis V12 studies.</p>
    <div class="photo photo--framed" role="img" aria-label="Photo of a smiling woman with blonde hair" style="margin-top:6px;height:60px;background:linear-gradient(180deg,#dfe9f1,#e9d2b6);"></div>
  </article>

  <article class="page page--references">
    <h2 class="heading">Th1/Th2 Cell Regulation</h2>
    <p class="lede">Supports sustained balancing of Th1 and Th2 cells.</p>
    <p class="physiology"><b>PHYSIOLOGY:</b> The T helper cells (Th1, Th2 and others) are a type of T cell that play an important role in the immune system, particularly in the adaptive immune system. They help the activity of other immune cells by releasing T cell cytokines. These cells help suppress or regulate immune responses. They are essential in B cell antibody class switching, in the activation and growth of cytotoxic T cells, and in maximizing bactericidal activity of phagocytes such as macrophages. Maintaining a balance between Th1 and Th2 cells is critical to a complete immune response, yet it is complicated by cross-regulation and imbalance in the stimuli.</p>
    <h2 class="heading">References:</h2>
    <ul class="refs">
      <li>Nutrient Concentrate and Process for Separating It from Early Milk Fractions (US Patent 9,104,552)</li>
      <li>Process for Raising Protective Proteins in Dairy Sources (US Patent 9,218,407)</li>
      <li>Bioactive Lacteal Complexes and Methods for Preparing Such Blends (Patent Application Pending)</li>
      <li>Meridian Clinical Associates. Vitalis V12 Within a Whole-Person Care Model for Natural Killer Cell Support in Long-Term Illness. March 2001.</li>
      <li>Lumen Research, Inc. Effects of Daily Vitalis V12 Intake on Natural Killer Cell Activity in Healthy Adults. Northgate Journal of Preventive Health, Vol 8, No 2, Apr 2011, 44-51.</li>
      <li>Keystone Immune Group. Review of Immune Response Markers in Healthy Volunteers Compared with a Lacteal Reference Study. Jun 2003</li>
      <li>Harlow, MB. Observations on Immune Response Balance in Adults Using Vitalis V12. Practitioner Review. 2008;17:33-39.</li>
      <li>Scientific References: Amino Acid Sequencing of Vitalis V12 at Eastbrook University</li>
      <li>Reyes P, Calder JT. A Pilot Study of a Lacteal Complex in a Murine Infection Model. Harbor Journal of Immune Studies. 14: 22-29, 2009.</li>
      <li>Varga L, Osei K. Lacteal complex supplementation and gene expression in laboratory mice. Applied Nutrient Reports. 2013;5:61-68.</li>
    </ul>
  </article>
</section>

<section class="spread spread--outside">
  <article class="page page--general-health">
    <h2 class="heading">General Health</h2>
    <p class="lede">Participants in a 90 day study report improved health and reduced symptomology.</p>
    <p class="physiology"><b>PHYSIOLOGY:</b> The benefits of utilizing dietary supplements are often not noted by the user, even if the benefits can be measured by some objective means. When a consumer experiences an objective or subjective sense of improvement in their general health they are more inclined to continue compliant supplementation. Participants in a study of Vitalis V12 were asked to complete Health Questionnaires covering a wide range of subjective health questions and symptoms. Participants reported a 32% reduction in perceived symptoms and other health issues at the conclusion of the study period through their completed questionnaires. This correlates to a significant reduction (p&lt;0.019).</p>
    <p>Anecdotal evidence, reports and consumer reorders and compliance all support the strong realization of benefit by consumers since 1994.</p>
    <div class="photo photo--framed" role="img" aria-label="Photo of a smiling young couple lying head to head on green grass with daisies" style="margin-top:6px;height:238px;background:linear-gradient(160deg,#9bbf5a 0%,#6f9a34 35%,#c9a27c 55%,#5e8a2c 100%);"></div>
  </article>

  <article class="page back-cover">
    <div class="photo" role="img" aria-label="Soft pattern of faint translucent dots over red"></div>
    <footer class="back-footer">
      <span>Northfield Nutrient Labs, LLC. 1200 Harbor View Rd, Suite 40 Dayton, OH 45402. 555 010-2040, 555 010-2041 FAX · www.vitalisv12.com</span>
      <span class="tab"></span>
    </footer>
  </article>

  <article class="page front-cover">
    <div class="photo" role="img" aria-label="Photo of a couple in silhouette kissing under a lace parasol against a golden sunset" style="background:linear-gradient(180deg,#c9d0d6 0%,#d6c7ae 35%,#f1c271 48%,#8d6c52 62%,#3a2a24 100%);"></div>
    <div class="tagline-band">
      <span class="tagline">High Priority Support for Immunity and Good Health</span>
      <span class="brand"><span class="mark"></span>Vitalis V12</span>
    </div>
  </article>
</section>

<div class="caption caption--bottom" style="left:180px">Inside 4th page</div>
<div class="caption caption--bottom" style="left:460px">back cover</div>
<div class="caption caption--bottom" style="left:740px">Front</div>

</body>
</html>
```